Professional DJ Business Card

Business card for giving out to clubs and venues or interested groups that are in need of a professional DJ. I want something artistic and catchy/alluring, with a minimalist approach that gets just the vital amount of info and leaves the rest for inquiry via contacting me. Ideally I would like one side to have an image of something cool like an eye and my name, then the other side be the contact info, I am definitely feeling a black or dark colored card, but I am open to other designs. I am uploading a picture that I made that reflects a little of what I am *kind of* looking for.

Industry/Entity Type

Business

Contact Information for Business Card

Tomas Halvik (Voxtel)
Professional DJ (West Coast)
EDM (Deep/House/Techno), Hip Hop, Latin, Trap.
Cell: 555-274-9163
Email: Voxtelofficial@mailnest.net
www.beatcloudia.net/yourtuneisfading

```html
<!DOCTYPE html>
<html lang="en">
<head>
<meta charset="utf-8">
<title>Voxtel – DJ Business Card</title>
<link rel="stylesheet" href="https://fonts.googleapis.com/css2?family=Gochi+Hand&display=swap">
<style>
  :root {
    --paper: #ffffff;
    --card-black: #040406;
    --neon-yellow: #f5ec1a;
    --yellow-light: #fff98a;
    --yellow-deep: #b8a600;
    --emblem-dim: #3a3505;
  }
  html, body {
    margin: 0;
    padding: 0;
    overflow: hidden;
    background: var(--paper);
  }
  .sheet {
    position: relative;
    width: 1200px;
    height: 848px;
    background: var(--paper);
    overflow: hidden;
  }
  .card {
    position: absolute;
    top: 280px;
    width: 462px;
    height: 263px;
    background: var(--card-black);
    box-shadow: 2px 3px 3px rgba(0,0,0,0.35);
    overflow: hidden;
  }
  .card--front { left: 82px; }
  .card--back { left: 621px; }
  .card__art {
    position: absolute;
    inset: 0;
    width: 100%;
    height: 100%;
  }
  .brand-name {
    position: absolute;
    left: 196px;
    top: 138px;
    margin: 0;
    font-family: "Gochi Hand", cursive;
    font-weight: 400;
    font-size: 58px;
    line-height: 1;
    color: var(--neon-yellow);
  }
  .contact {
    position: absolute;
    left: 185px;
    top: 107px;
    margin: 0;
    padding: 0;
    list-style: none;
    font-family: "Gochi Hand", cursive;
    font-size: 11.5px;
    line-height: 20px;
    color: var(--neon-yellow);
    white-space: nowrap;
  }
  .emblem-slot {
    position: absolute;
    left: 280px;
    top: 6px;
    width: 170px;
    height: 100px;
    border-radius: 50%;
    background: radial-gradient(ellipse at center, var(--emblem-dim) 0%, var(--card-black) 70%);
  }
</style>
</head>
<body>
<main class="sheet">

  <section class="card card--front" aria-label="Card front">
    <svg class="card__art" viewBox="0 0 462 263" aria-hidden="true">
      <defs>
        <linearGradient id="band-front" x1="0" y1="0" x2="0" y2="1">
          <stop offset="0" stop-color="var(--yellow-light)"/>
          <stop offset="0.5" stop-color="var(--neon-yellow)"/>
          <stop offset="1" stop-color="var(--yellow-deep)"/>
        </linearGradient>
      </defs>
      <rect class="band band--top" x="0" y="0" width="462" height="25" fill="url(#band-front)"/>
      <rect class="band band--bottom" x="0" y="238" width="462" height="25" fill="url(#band-front)"/>
      <polygon class="stripe" points="0,30 0,48 100,238 114,238" fill="url(#band-front)"/>
      <polygon class="stripe" points="12,25 28,25 140,238 124,238" fill="url(#band-front)"/>
      <polygon class="stripe" points="40,25 56,25 168,238 152,238" fill="url(#band-front)"/>
    </svg>
    <h1 class="brand-name">Voxtel</h1>
  </section>

  <section class="card card--back" aria-label="Card back">
    <svg class="card__art" viewBox="0 0 462 263" aria-hidden="true">
      <defs>
        <linearGradient id="band-back" x1="0" y1="0" x2="0" y2="1">
          <stop offset="0" stop-color="var(--yellow-light)"/>
          <stop offset="0.5" stop-color="var(--neon-yellow)"/>
          <stop offset="1" stop-color="var(--yellow-deep)"/>
        </linearGradient>
      </defs>
      <rect class="band band--bottom" x="0" y="238" width="462" height="25" fill="url(#band-back)"/>
      <polygon class="stripe" points="0,8 0,28 100,238 114,238" fill="url(#band-back)"/>
      <polygon class="stripe" points="8,0 24,0 138,238 122,238" fill="url(#band-back)"/>
      <polygon class="stripe" points="32,0 48,0 172,238 156,238" fill="url(#band-back)"/>
    </svg>
    <div class="emblem-slot" role="img" aria-label="Voxtel emblem area"></div>
    <ul class="contact">
      <li>Tomas Halvik (Voxtel)</li>
      <li>Professional DJ (West Coast)</li>
      <li>EDM (Deep/House/Techno), Hip Hop, Latin, Trap.</li>
      <li>Cell: 555-274-9163</li>
      <li>Email: Voxtelofficial@mailnest.net</li>
      <li>www.beatcloudia.net/yourtuneisfading</li>
    </ul>
  </section>

</main>
</body>
</html>
```